Bright Path Flyer Design for Virtual Online Clinic. -5.5 x 8.5 inches (half sheet)

We need a clean, modern flyer design for Bright Path, a new virtual walk-in clinic based in British Columbia. The flyer will be used in libraries, pharmacies, and community centers to help residents easily access primary care through their Bright Path NFC access card.
The flyer will ask a question : NEED A DOCTOR? This should be large and attention grabbing.
The design should clearly feature a Bright Path card image (the access card) as the centerpiece and visually show how patients can use it to book appointments. The tone should feel trustworthy, healthcare-oriented, and community-friendly — clean fonts, clear spacing, and strong readability from a distance.

Side One: This card has the NFC Access Card.
NEED A DOCTOR? (Large Font, Attention Grabbing)
How to Book an Appointment using your Bright Path Card
Step 1: Tap Your Card on Your Phone
Hold your card near the back of your phone.
It will activate automatically — no app needed.
The Bright Path scheduler will open.
Step 2: Schedule Your Appointment
Select your clinical concern.
Choose your time window.
Register (only once).
Confirm your appointment.
Step 3: Relax, we’ll take care of the rest
A doctor will call during your scheduled time.
Once booked, you’ll be able to call our office.
No emails, no texts — just a real person.
It’s that simple.
Side Two:
About Bright Path
Created by Dr. Marcus Ferrigan
Bright Path was founded to make healthcare simple and convenient. Prescription renewals. Common infections. Medical notes. And so much more.
Our doctors can address 120+ health concerns virtually — providing quality care without the waiting room. No waiting rooms. Just real doctors providing real care.
Why Patients Choose Bright Path
Easy access – book and be seen from anywhere in BC.
Effortless booking – tap your Bright Path Card to begin.
Trusted physicians – every visit is with a licensed BC family doctor.
How It Works
Book your visit — choose a time window that fits your day.
Join the queue — you’ll be called when it’s your turn.
Speak directly with your doctor — simple, secure, and stress-free.
Convenient Care for Common Concerns

Additional Details.
Please find the domain to be launched soon. I've attached the NFC card file for review, it is 85.5 mm x 54 mm. The card will be glued to the flyer.
I've attached examples of flyers but they are not the look I am seeking and I am looking for creative solutions.
Thank you!
http://brightpath-example.test/

Adult Patients in British Columbia

Healthcare

• Looking for clean lines, uniform appearance, and high legibility i.e poppins

0054AA
0677BA
7BADD7
CADEEF
E8F1F8

• Need A Doctor?
• Elegant style, not too busy, clear layout.
• Clutter, look cheap - review examples.

```html
<!DOCTYPE html>
<html lang="en">
<head>
<meta charset="utf-8">
<title>Bright Path – Flyer</title>
<link href="https://fonts.googleapis.com/css2?family=Arimo:wght@400;700&display=swap" rel="stylesheet">
<style>
  :root{
    --navy:#2d3473;
    --navy-deep:#272d66;
    --teal:#1b98c4;
    --teal-light:#7badd7;
    --ink:#4a4c55;
    --grey-fade:#e4e5e9;
    --backdrop:#7a7978;
    --paper:#ffffff;
  }
  *{box-sizing:border-box;margin:0;padding:0}
  html,body{width:1200px;height:996px;overflow:hidden}
  body{background:var(--backdrop);font-family:"Arimo",Arial,sans-serif;color:var(--ink);position:relative}

  .flyer{position:absolute;width:496px;height:767px;background:var(--paper);box-shadow:6px 8px 14px rgba(0,0,0,.35);overflow:hidden}
  .flyer--front{left:75px;top:111px}
  .flyer--back{left:622px;top:109px}

  .header-art{position:absolute;left:0;top:0;width:496px;height:320px}
  .abs{position:absolute}

  .brand-name{position:absolute;color:#fff;font-weight:400;font-size:40px;letter-spacing:.5px;white-space:nowrap}
  .headline{position:absolute;left:0;width:496px;top:124px;text-align:center;color:#fff;font-weight:700;font-size:31px;letter-spacing:.6px}

  /* access card */
  .access-card{position:absolute;left:83px;top:186px;width:329px;height:193px;background:#d6d8dc;padding:4px;box-shadow:0 6px 16px rgba(27,152,196,.45)}
  .access-card__face{position:relative;width:100%;height:100%;background:#fff;overflow:hidden}
  .access-card__panel{position:absolute;left:0;top:0}
  .access-card__name{position:absolute;left:110px;top:72px;color:var(--navy);font-size:26px;font-weight:400;letter-spacing:.3px}
  .access-card__chip{position:absolute;right:14px;top:14px;width:12px;height:12px;background:var(--navy)}
  .access-card__tap{position:absolute;right:18px;bottom:16px;display:flex;align-items:center;gap:7px;font-size:9.5px;color:var(--navy)}

  .section-title{position:absolute;left:0;width:100%;text-align:center;font-size:14.5px;letter-spacing:1px;line-height:17px}
  .section-title .teal{color:var(--teal)}
  .section-title .navy{color:var(--navy)}

  .col{position:absolute;background:linear-gradient(90deg,rgba(255,255,255,0) 80%,var(--grey-fade) 100%)}
  .col--last{background:linear-gradient(90deg,rgba(255,255,255,0) 85%,var(--grey-fade) 100%)}
  .step-label{display:flex;align-items:center;gap:6px;color:var(--navy);font-size:12.5px;letter-spacing:.6px;height:18px}
  .step-sub{color:var(--teal);font-size:11.5px;letter-spacing:.6px;line-height:13.7px;margin-top:6px}
  .checks{list-style:none;margin-top:9px}
  .checks li{position:relative;padding-left:12px;font-size:11px;letter-spacing:.55px;line-height:13.6px;margin-bottom:13.5px}
  .checks li::before{content:"✓";position:absolute;left:0;top:0;color:var(--teal);font-size:10px}

  .pill{position:absolute;background:var(--navy);color:#fff;border-radius:14px;text-align:center;font-size:12.5px;letter-spacing:.8px}
  .sprig{position:absolute;width:30px;height:24px;background:var(--teal);opacity:.75;border-radius:50% 50% 50% 0}

  .help{position:absolute;left:0;width:100%;text-align:center;color:var(--navy);font-size:12.2px;line-height:18px}
  .help .contact{display:flex;justify-content:center;gap:18px}
  .help .contact span{display:inline-flex;align-items:center;gap:4px}

  /* back */
  .about{position:absolute;left:152px;top:122px;width:320px;color:#fff}
  .about__by{font-size:15px;letter-spacing:.2px}
  .about p{font-size:11px;letter-spacing:.5px;line-height:13.5px;margin-top:12px}
  .about p + p{margin-top:14px}

  .feature-title{display:flex;align-items:flex-start;gap:6px;color:var(--navy);font-size:12.5px;letter-spacing:.6px;line-height:15px}
  .feature-body{font-size:11px;letter-spacing:.55px;line-height:13.6px;margin-top:13px}
  .flow-title{color:var(--navy);font-size:12.5px;letter-spacing:.6px;line-height:15px;white-space:nowrap}
  .flow-body{font-size:11px;letter-spacing:.55px;line-height:13.6px}
</style>
</head>
<body>

<!-- FRONT -->
<section class="flyer flyer--front">
  <svg class="header-art" viewBox="0 0 496 320" role="img" aria-label="Photo of a caregiver holding a patient's hand, tinted in soft navy">
    <defs>
      <linearGradient id="frontTint" x1="0" y1="0" x2="1" y2="0.3">
        <stop offset="0" stop-color="#cfc7d3"/>
        <stop offset=".35" stop-color="#8b84a8"/>
        <stop offset=".7" stop-color="#3f4482"/>
        <stop offset="1" stop-color="#2d3473"/>
      </linearGradient>
    </defs>
    <path d="M0 0H496V292C440 278 380 282 300 292C200 304 80 318 0 262Z" fill="url(#frontTint)"/>
    <path d="M0 262C80 318 200 304 300 292C380 282 440 278 496 292V296C440 284 380 288 300 298C200 310 80 326 0 270Z" fill="var(--navy)"/>
    <path d="M0 270C80 326 200 310 300 298C380 288 440 284 496 296V300C440 290 380 294 300 303C200 316 80 332 0 276Z" fill="var(--teal)"/>
  </svg>

  <div class="brand-name" style="left:130px;top:60px;">Bright Path</div>
  <h1 class="headline">NEED A DOCTOR?</h1>

  <div class="access-card">
    <div class="access-card__face">
      <svg class="access-card__panel" width="140" height="185" viewBox="0 0 140 185" role="img" aria-label="Patterned navy side panel of the access card">
        <path d="M0 0H136C96 40 70 90 78 130C82 155 70 170 80 185H0Z" fill="var(--navy)"/>
      </svg>
      <span class="access-card__chip"></span>
      <div class="access-card__name">Bright Path</div>
      <div class="access-card__tap">Tap Here to Book
        <svg width="26" height="18" viewBox="0 0 26 18"><rect x="1" y="2" width="14" height="14" rx="2" fill="none" stroke="var(--navy)" stroke-width="1.4"/><rect x="4" y="6" width="8" height="6" fill="var(--navy)"/><path d="M17 5q3 4 0 8M20 3q5 6 0 12" fill="none" stroke="var(--navy)" stroke-width="1.6"/></svg>
      </div>
    </div>
  </div>

  <div class="section-title" style="top:404px;"><div class="teal">HOW TO BOOK AN APPOINTMENT</div><div class="navy">USING YOUR BRIGHT PATH CARD</div></div>

  <div class="col" style="left:0;top:446px;width:163px;height:205px;padding:12px 0 0 12px;">
    <div class="step-label" style="padding-left:12px;">STEP 1
      <svg width="26" height="16" viewBox="0 0 26 16"><rect x="1" y="1" width="17" height="11" rx="1" fill="none" stroke="var(--navy)" stroke-width="1.2"/><path d="M10 14l6-6 8 5-3 3" fill="none" stroke="var(--navy)" stroke-width="1.2"/></svg>
    </div>
    <div class="step-sub" style="padding-left:12px;">Tap Your Card on<br>Your Phone</div>
    <ul class="checks">
      <li>Hold your card near the back of your phone.</li>
      <li>It will activate automatically - no app needed.</li>
      <li>The Bright Path scheduler will open.</li>
    </ul>
  </div>

  <div class="col" style="left:163px;top:446px;width:171px;height:205px;padding:12px 0 0 8px;">
    <div class="step-label" style="padding-left:12px;">STEP 2
      <svg width="20" height="17" viewBox="0 0 20 17"><rect x="1" y="3" width="18" height="13" rx="1.5" fill="none" stroke="var(--navy)" stroke-width="1.2"/><path d="M5 1v4M15 1v4M1 6h18M6 11l3 3 5-5" fill="none" stroke="var(--navy)" stroke-width="1.2"/></svg>
    </div>
    <div class="step-sub" style="padding-left:12px;">Schedule Your<br>Appointment</div>
    <ul class="checks">
      <li>Select your clinical concern.</li>
      <li>Choose your time window.</li>
      <li>Register (only once).</li>
      <li>Confirm your appointment.</li>
    </ul>
  </div>

  <div class="col col--last" style="left:334px;top:446px;width:162px;height:205px;padding:12px 0 0 3px;">
    <div class="step-label" style="padding-left:12px;">STEP 3
      <svg width="28" height="16" viewBox="0 0 28 16"><circle cx="14" cy="6" r="4" fill="none" stroke="var(--navy)" stroke-width="1.2"/><path d="M2 4l5 3 3 6M26 4l-5 3-3 6M8 14h12" fill="none" stroke="var(--navy)" stroke-width="1.2"/></svg>
    </div>
    <div class="step-sub" style="padding-left:12px;">Relax, we’ll take care<br>of the rest</div>
    <ul class="checks">
      <li>A doctor will call during your scheduled time.</li>
      <li>Once booked, you’ll be able to call our office.</li>
      <li>No emails, no texts - just a real person.</li>
    </ul>
  </div>

  <div class="pill" style="left:171px;top:662px;width:153px;height:28px;line-height:28px;">It’s that Simple</div>
  <span class="sprig" role="img" aria-label="Small teal leaf sprig" style="left:330px;top:664px;"></span>

  <div class="help" style="top:712px;">
    <div>If you’re having trouble with your card or the access page, we’re here to help:</div>
    <div class="contact">
      <span><svg width="11" height="8" viewBox="0 0 11 8"><rect width="11" height="8" fill="var(--navy)"/><path d="M0 0l5.5 4.5L11 0" fill="none" stroke="#fff" stroke-width="1"/></svg>support@brightpath-example.test</span>
      <span><svg width="8" height="9" viewBox="0 0 8 9"><path d="M0 0l8 4-3 1 2 3-1 1-2-3-2 2z" fill="var(--navy)"/></svg>www.brightpath-example.test</span>
    </div>
  </div>
</section>

<!-- BACK -->
<section class="flyer flyer--back">
  <svg class="header-art" viewBox="0 0 496 320" role="img" aria-label="Photo of a physician in a white coat with a stethoscope, blended into navy">
    <defs>
      <linearGradient id="backTint" x1="0" y1="0" x2="1" y2="0">
        <stop offset="0" stop-color="#dfe4ee"/>
        <stop offset=".22" stop-color="#aeb7cf"/>
        <stop offset=".45" stop-color="#4a5190"/>
        <stop offset=".6" stop-color="#2d3473"/>
        <stop offset="1" stop-color="#2d3473"/>
      </linearGradient>
    </defs>
    <path d="M0 0H496V288C430 270 300 284 200 298C120 308 50 300 0 262Z" fill="url(#backTint)"/>
    <path d="M0 262C50 300 120 308 200 298C300 284 430 270 496 288V296C430 280 300 294 200 306C120 316 50 310 0 272Z" fill="var(--navy)"/>
    <path d="M0 272C50 310 120 316 200 306C300 294 430 280 496 296V302C430 288 300 302 200 313C120 322 50 318 0 280Z" fill="var(--teal)"/>
  </svg>

  <div class="brand-name" style="left:152px;top:64px;">Bright Path</div>

  <div class="about">
    <div class="about__by">Created by Dr. Marcus Ferrigan</div>
    <p>Bright Path was founded to make healthcare simple and convenient. Prescription renewals. Common infections. Medical notes. And so much more.</p>
    <p>Our doctors can address 120+ health concerns virtually - providing quality care without the waiting room.<br>No waiting rooms. <em>Just real doctors providing real care.</em></p>
  </div>

  <div class="section-title" style="top:336px;"><div class="teal">WHY PATIENTS CHOOSE BRIGHT PATH</div></div>

  <div class="col" style="left:0;top:366px;width:167px;height:99px;padding:16px 0 0 27px;">
    <div class="feature-title">
      <svg width="24" height="24" viewBox="0 0 24 24"><circle cx="11" cy="11" r="10" fill="none" stroke="var(--navy)" stroke-width="1.3"/><path d="M6 11l3 3 6-6" fill="none" stroke="var(--navy)" stroke-width="1.3"/><rect x="15" y="15" width="7" height="6" fill="#fff" stroke="var(--navy)" stroke-width="1.2"/></svg>
      <span>EASY<br>ACCESS</span>
    </div>
    <div class="feature-body">Book and be seen<br>from anywhere in BC.</div>
  </div>

  <div class="col" style="left:167px;top:366px;width:148px;height:99px;padding:16px 0 0 11px;">
    <div class="feature-title">
      <svg width="24" height="24" viewBox="0 0 24 24"><rect x="2" y="4" width="20" height="18" rx="2" fill="none" stroke="var(--navy)" stroke-width="1.3"/><path d="M7 1v5M17 1v5M2 8h20" stroke="var(--navy)" stroke-width="1.3"/><circle cx="12" cy="15" r="4.5" fill="none" stroke="var(--navy)" stroke-width="1.2"/><path d="M10 15l1.5 1.5 3-3" fill="none" stroke="var(--navy)" stroke-width="1.2"/></svg>
      <span>EFFORTLESS<br>BOOKING</span>
    </div>
    <div class="feature-body">Tap your Bright Path<br>Card to begin.</div>
  </div>

  <div class="col col--last" style="left:315px;top:366px;width:181px;height:99px;padding:16px 0 0 13px;">
    <div class="feature-title">
      <svg width="24" height="24" viewBox="0 0 24 24"><path d="M12 1l9 4v7c0 6-4 9-9 11C7 21 3 18 3 12V5z" fill="none" stroke="var(--navy)" stroke-width="1.3"/><path d="M12 8v8M8 12h8" stroke="var(--navy)" stroke-width="2"/></svg>
      <span>TRUSTED<br>PHYSICIANS</span>
    </div>
    <div class="feature-body">Every visit is with a<br>licensed BC family doctor.</div>
  </div>

  <div class="section-title" style="top:489px;"><div class="teal">HOW IT WORKS</div></div>

  <div class="col" style="left:0;top:522px;width:167px;height:99px;padding:10px 0 0 28px;">
    <div class="flow-title">BOOK YOUR VISIT <span style="letter-spacing:-1px">⟶</span></div>
    <div class="flow-body" style="margin-top:20px;">Choose a time window<br>that fits your day.</div>
  </div>
  <div class="col" style="left:167px;top:522px;width:148px;height:99px;padding:10px 0 0 11px;">
    <div class="flow-title">JOIN THE QUEUE <span style="letter-spacing:-1px">⟶</span></div>
    <div class="flow-body" style="margin-top:20px;">You’ll be called<br>when it’s your turn.</div>
  </div>
  <div class="col col--last" style="left:315px;top:522px;width:181px;height:99px;padding:10px 0 0 13px;">
    <div class="flow-title">SPEAK DIRECTLY WITH<br>YOUR DOCTOR</div>
    <div class="flow-body" style="margin-top:8px;">Simple, secure, and<br>stress-free.</div>
  </div>

  <div class="pill" style="left:97px;top:651px;width:302px;height:27px;line-height:27px;">Convenient Care for Common Concerns</div>
  <span class="sprig" role="img" aria-label="Small teal leaf sprig" style="left:406px;top:652px;"></span>

  <div class="help" style="top:705px;">
    <div>If you’re having trouble with your card or the access page, we’re here to help:</div>
    <div class="contact">
      <span><svg width="11" height="8" viewBox="0 0 11 8"><rect width="11" height="8" fill="var(--navy)"/><path d="M0 0l5.5 4.5L11 0" fill="none" stroke="#fff" stroke-width="1"/></svg>support@brightpath-example.test</span>
      <span><svg width="8" height="9" viewBox="0 0 8 9"><path d="M0 0l8 4-3 1 2 3-1 1-2-3-2 2z" fill="var(--navy)"/></svg>www.brightpath-example.test</span>
    </div>
  </div>
</section>

</body>
</html>
```